Business card design needed

Need a new business card design for a new business in Sydney, Australia called 'Tarrow Australia'. The business deals in consulting for new sales, sales leadership and customer service consultancy. Want the business card to look professional and clean

Industry/Entity Type

Leadership

Contact Information for Business Card

Tarrow Australia
Peter Holm
Managing Director

14 Corvane Street
Brackmere NSW 2095

0455 913 702
peter@tarrow.com.au
www.tarrow.com.au

```html
<!DOCTYPE html>
<html lang="en">
<head>
<meta charset="utf-8">
<title>Peter Holm – Tarrow Australia Business Card</title>
<link rel="stylesheet" href="https://fonts.googleapis.com/css2?family=Comic+Neue:wght@400;700&display=swap">
<style>
  :root {
    --ink-white: #ffffff;
    --card-black: #000000;
    --panel-light: #5b5d5c;
    --panel-dark: #434343;
    --silver-light: #f2f2f2;
    --silver-mid: #bdbdbd;
    --silver-dark: #8e8e8e;
    --accent-red: #e01b1b;
    --page-bg: #ffffff;
  }
  html, body {
    margin: 0;
    padding: 0;
    width: 1200px;
    height: 699px;
    overflow: hidden;
    background: var(--page-bg);
  }
  .card {
    position: relative;
    width: 1200px;
    height: 699px;
    background: var(--card-black);
    overflow: hidden;
    font-family: "Comic Neue", "Comic Sans MS", cursive;
    color: var(--ink-white);
  }
  .silver-strip {
    position: absolute;
    left: 0; top: 0;
    width: 53px; height: 699px;
    background: linear-gradient(100deg, var(--silver-dark) 0%, var(--silver-light) 35%, var(--silver-mid) 55%, var(--silver-light) 75%, var(--silver-dark) 100%);
  }
  .name-panel {
    position: absolute;
    left: 53px; top: 0;
    width: 548px; height: 699px;
    background: linear-gradient(90deg, var(--panel-light) 0%, var(--panel-dark) 100%);
  }
  .divider {
    position: absolute;
    left: 580px; top: 0;
    width: 40px; height: 699px;
  }
  .identity {
    position: absolute;
    left: 53px; width: 622px;
    top: 290px;
    text-align: center;
    transform: translateX(-132px);
  }
  .identity__name {
    margin: 0;
    font-weight: 700;
    font-size: 48px;
    line-height: 1;
    letter-spacing: 0.5px;
  }
  .identity__role {
    margin: 14px 0 0;
    font-weight: 400;
    font-size: 33px;
    line-height: 1;
  }
  .contacts {
    position: absolute;
    left: 627px; top: 212px;
    margin: 0; padding: 0;
    list-style: none;
  }
  .contact {
    display: flex;
    align-items: center;
    height: 40px;
    font-size: 28px;
  }
  .contact + .contact { margin-top: 36px; }
  .contact--email { margin-top: 42px !important; }
  .contact__icon {
    width: 38px; height: 38px;
    margin-right: 14px;
    flex: none;
  }
</style>
</head>
<body>
  <main class="card">
    <div class="silver-strip"></div>
    <div class="name-panel"></div>

    <svg class="divider" viewBox="0 0 40 699" aria-hidden="true">
      <path d="M21 39 Q0 349 21 659 L40 659 L40 39 Z" fill="var(--accent-red)"/>
      <path d="M21 0 L21 39 Q5 349 21 659 L21 699 L40 699 L40 0 Z" fill="var(--card-black)"/>
    </svg>

    <section class="identity">
      <h1 class="identity__name">Peter Holm</h1>
      <p class="identity__role">Managing Director</p>
    </section>

    <ul class="contacts">
      <li class="contact">
        <svg class="contact__icon" viewBox="0 0 24 24" aria-hidden="true">
          <path d="M12 2 L1 12 L4 12 L4 22 L10 22 L10 15 L14 15 L14 22 L20 22 L20 12 L23 12 Z M12 5.5 L18 11 L18 20 L16 20 L16 13 L8 13 L8 20 L6 20 L6 11 Z" fill="var(--ink-white)"/>
        </svg>
        <span>14 Corvane Street Brackmere NSW 2095</span>
      </li>
      <li class="contact">
        <svg class="contact__icon" viewBox="0 0 24 24" aria-hidden="true">
          <path d="M6.6 2.5 L9.5 6.8 C9.9 7.4 9.8 8.1 9.3 8.6 L8 9.8 C9.2 12.4 11.6 14.8 14.2 16 L15.4 14.7 C15.9 14.2 16.6 14.1 17.2 14.5 L21.5 17.4 C22.1 17.8 22.2 18.6 21.8 19.2 L20.3 21 C19.6 21.8 18.5 22.1 17.5 21.8 C10.3 19.6 4.4 13.7 2.2 6.5 C1.9 5.5 2.2 4.4 3 3.7 L4.8 2.2 C5.4 1.8 6.2 1.9 6.6 2.5 Z" fill="var(--ink-white)"/>
        </svg>
        <span>0455 913 702</span>
      </li>
      <li class="contact contact--email">
        <svg class="contact__icon" viewBox="0 0 24 24" aria-hidden="true">
          <path d="M1 5 L23 5 L12 13.5 Z" fill="var(--ink-white)"/>
          <path d="M1 7.5 L12 16 L23 7.5 L23 19 L1 19 Z" fill="var(--ink-white)"/>
        </svg>
        <span>peter@tarrow.com.au</span>
      </li>
      <li class="contact">
        <svg class="contact__icon" viewBox="0 0 24 24" aria-hidden="true">
          <circle cx="12" cy="12" r="10.5" fill="var(--ink-white)"/>
          <g stroke="var(--card-black)" stroke-width="1.4" fill="none">
            <ellipse cx="12" cy="12" rx="4.5" ry="10.5"/>
            <line x1="12" y1="1.5" x2="12" y2="22.5"/>
            <line x1="1.5" y1="12" x2="22.5" y2="12"/>
            <line x1="3" y1="7" x2="21" y2="7"/>
            <line x1="3" y1="17" x2="21" y2="17"/>
          </g>
        </svg>
        <span>www.tarrow.com.au</span>
      </li>
    </ul>
  </main>
</body>
</html>
```